Individual Needs Design for Marketing Package

****IMPORTANT: Note that I have arranged an agreement with a specific designer to complete the design for the portfolio. Please do not submit any designs***

Goal
I recently resigned from my job in Canada, and I am moving down to Silicon Valley to pursue a career in the technology startup scene - initially doing technical sales. So my goal is to get a sales position with a startup tech company.

In order to land a sales position, I will be going to a startup conference in Silicon Valley which brings together over 2,000 startup technology companies. My goal is to meet the owners of some of these companies and demonstrate that I can be a valuable asset to their company. My challenge is that I have no existing relationships in Silicon Valley and limited experience in sales. So I have put together a portfolio of some of my most significant accomplishments over the past 6 years (see attached file). My hope is that this portfolio will convey that even though I have limited experience, I am passionate, driven, and loyal with a proven track record of achievement. After talking with them for 30 minutes and developing a rapport, I plan on giving this accomplishment portfolio (in addition to my resume) to CEOs of companies for which I could potentially work.

Message to Communicate
After someone reads my portfolio, I want them to view me as passionate, driven, and loyal with a proven track record of achievement. The design can communicate this message in a subtle way. The portfolio should also speak to my professionalism. It should certainly have some personality, but it should err on the side of professionalism.

Competitors
My competitors will be other people at the conference also looking to get sales positions with these startup companies. My main points of differentiation are that I am passionate, driven, and loyal with a proven track record of results. I would like this to be made a feature of the design.

Design Templates
I do not have any specific fonts or colours that I need you to use. The colours scheme and fonts selected should reinforce my key message.

Other Information
I do not own any specialized design software - only the basic microsoft word and powerpoint. However, I will need to be able to add new accomplishments to the portfolio and edit existing ones. Please let me know how this will be possible. I am not sure if it is possible to convert the final file into a file format that I can edit.

Notice that I have arranged the pages into sections. Feel free to rearrange the content within the sections, but please do not change the order of the sections

The size for the marketing package will be regular 8.5 x 11".
Updates

Target Market(s)

The people that will be reading my portfolio are owners of small technology companies in Silicon Valley. They are typically 28-35 years old, and highly logical thinkers. This means that the content is what is ultimately going to sell myself, but the design is what will make them want to read it. Therefore, the content should really stand out over the design.

Industry/Entity Type

Marketing

Requirements
Must have
• ****IMPORTANT: Note that I have arranged an agreement with a specific designer to complete the design for the portfolio. Please do not submit any designs***

I really view this portfolio as my personal marketing package, and that is where I need your expertise. I need you to take the content that I have in my portfolio and turn it into a personal marketing package. I need you to:

1. Design the cover page
2. Design the template for the content pages
3. Format the pictures and text to best fit the design of the pages**

** I would like the final design submission to include the pictures and text included in the attached file all fully formatted. However, when submitting the first iterations, please do not feel obligated to format the entire portfolio because I know that it can be time consuming. Just formatting the title page and the first content page should be enough to give me an idea of what the final portfolio will look like. Once we narrow it down to the final few designs, then we can start formatting the complete portfolio.

```html
<!DOCTYPE html>
<html lang="en">
<head>
<meta charset="utf-8">
<title>Accomplishments – Page 7</title>
<link href="https://fonts.googleapis.com/css2?family=Gelasio:wght@400;500&display=swap" rel="stylesheet">
<style>
  :root {
    --page-bg: #e6e7e9;
    --navy: #0f3557;
    --red: #a3101c;
    --shadow: #1c1c1c;
    --text: #1c3a5e;
    --white: #ffffff;
  }
  * { margin: 0; padding: 0; box-sizing: border-box; }
  html, body { width: 927px; height: 1200px; overflow: hidden; }
  body {
    background: var(--page-bg);
    font-family: "Gelasio", Georgia, serif;
    color: var(--text);
    position: relative;
  }
  .page-tab { position: absolute; top: 0; right: 0; width: 109px; height: 108px; }
  .page-tab .bar { position: absolute; background: var(--navy); }
  .page-tab .bar-top { left: 0; top: 0; width: 109px; height: 32px; }
  .page-tab .bar-side { right: 0; top: 0; width: 33px; height: 108px; }
  .page-number {
    position: absolute; left: 0; top: 44px; width: 65px; height: 64px;
    background: var(--red); color: var(--white);
    font-size: 24px; display: flex; align-items: center; justify-content: center;
    font-variant-numeric: lining-nums;
  }
  .feature { position: absolute; left: 87px; width: 840px; height: 370px; }
  .feature-one { top: 212px; }
  .feature-two { top: 642px; }
  .feature-frame { position: absolute; left: 0; top: 0; }
  .photo { position: absolute; left: 11px; top: 11px; width: 502px; height: 335px; }
  .photo-football {
    background: linear-gradient(180deg, #a9a79f 0%, #8f918f 30%, #6f7a78 42%, #2f6b3a 62%, #2c6a35 100%);
  }
  .photo-relay {
    background: linear-gradient(180deg, #e4e6e8 0%, #3e5540 22%, #6a6156 45%, #4d6b3a 70%, #3f6230 100%);
  }
  .feature-copy {
    position: absolute; left: 570px;
    font-size: 17px; line-height: 20.5px;
    font-variant-numeric: oldstyle-nums;
  }
  .feature-one .feature-copy { top: 80px; }
  .feature-two .feature-copy { top: 82px; }
  .feature-copy p + p { margin-top: 20.5px; }
</style>
</head>
<body>
  <div class="page-tab">
    <div class="bar bar-top"></div>
    <div class="bar bar-side"></div>
    <div class="page-number">7</div>
  </div>

  <section class="feature feature-one">
    <svg class="feature-frame" width="560" height="370" viewBox="0 0 560 370">
      <path d="M5 5 H529 V73 L558 90 L529 107 V363 H5 Z" fill="var(--shadow)"/>
      <path d="M0 0 H524 V68 L553 85 L524 102 V358 H0 Z" fill="var(--red)"/>
    </svg>
    <div class="photo photo-football" role="img" aria-label="Team photo of the bantam football players and coaches on the field"></div>
    <div class="feature-copy">
      <p>I coached bantam football<br>for 2 years. In our inaugural<br>season, we were 0-7 with<br>351 points against and<br>0 points for.</p>
      <p>In our second season, 90%<br>of our players returned to<br>the team and we were<br>4-3 with 250 points for and<br>190 points against.</p>
    </div>
  </section>

  <section class="feature feature-two">
    <svg class="feature-frame" width="560" height="370" viewBox="0 0 560 370">
      <path d="M5 5 H529 V78 L558 95 L529 112 V363 H5 Z" fill="var(--shadow)"/>
      <path d="M0 0 H524 V73 L553 90 L524 107 V358 H0 Z" fill="var(--red)"/>
    </svg>
    <div class="photo photo-relay" role="img" aria-label="Fundraising walk team posing outdoors with their team banner"></div>
    <div class="feature-copy">
      <p>For three years, I was<br>involved in Walk for Hope<br>to help raise money for<br>the Northern Cancer Fund.<br>I was our team captain<br>in 2009.</p>
      <p>We raised the following<br>amounts each year:<br>2008 - $7,500<br>2009 - $8,500<br>2010 - $4,500</p>
    </div>
  </section>
</body>
</html>
```